Elderberry syrup- company product label for placement in grocery chain

I need a label for my elderberry syrup. Trying to decide if I want a logo for each individual product or If I want a label that can be edited from Elderberry Syrup to Elderberry gummies, Elderberry Jam, Etc. I will also need to be able to edit it to different sizes (8oz, 16oz) and edit the ingredients from Honey to Maple Syrup, etc.and remove statements such as "not safe for children under 1" on products that are safe.
I have a couple of competitors in my area. I have included the link to one here: https://www.brambleknollsyrup.com/our-syrup/
And attached a copy of the label of another. I need to have a front and back label or a wrap around label with all the information.

Front: Logo, Elderberry Syrup, 8 fl oz/236 ml, Organic Ingredients, Local honey, Cold-Flu-Allergies, Natural Remedy, Hand Crafted

Back: Ingredients (Organic Elderberries, water, Organic cinnamon, Organic Clove, Organic Ginger, L-ascorbic acid (vit C), Honey

Suggested Use:
Children: 1 tsp (or teaspoon)
Adults: 1 tbsp. (or tablespoon)
preventative: Once daily
When sick: every 3 hours

Other info optional where on labels: Pellham, NC
Refrigerate after opening
Made in NC by Hollow Creek Tonics, LLC
www.hctelderberry.com

*Not safe for children under age 1
*This statement has not been evaluated by the FDA

Barcode

* The bottles used are glass amber bottles.
Possible label ideas are 'kraft' look label, white label, vintage looking label, apothecary looking label. This is a holistic/naturalistic product and the label needs to reflect that.

* I attached my current label as reference for the professional but not commercial look, although my current label is far from professional.

*Logo does not have to be in color. Label can be in black/kraft colors if need be. (Example: bramble knoll syrup label)

Target Market(s)

Holistic/naturalistic crowd

Font styles to use
Sans Serif
Other font styles liked:
• Antipasto to match logo

Colors

Designer to choose colors to be used in the design.

Requirements
Nice to have
• A professional but not commercial look. This is a handcrafted item.

```html
<!DOCTYPE html>
<html lang="en">
<head>
<meta charset="utf-8">
<title>Elderberry Syrup Label</title>
<link rel="stylesheet" href="https://fonts.googleapis.com/css2?family=Questrial&family=Barlow:wght@600&display=swap">
<style>
  :root {
    --backdrop: #d3e3ea;
    --label-white: #ffffff;
    --leaf-green: #a9c79a;
    --berry-blue: #4d5a75;
    --ring: #e9ebef;
    --disc-top: #cfe5f0;
    --disc-bottom: #f3f9fc;
    --ink: #5a6178;
    --brand: #5d2f63;
    --size-chip: #e4f1f7;
  }
  html, body {
    margin: 0;
    width: 1200px;
    height: 1144px;
    overflow: hidden;
    background: var(--backdrop);
  }
  .label {
    position: absolute;
    left: 322px;
    top: 241px;
    width: 582px;
    height: 685px;
    background: var(--label-white);
    overflow: hidden;
  }
  .botanical-art {
    position: absolute;
    inset: 0;
    background:
      radial-gradient(circle at 12% 18%, var(--berry-blue) 0 3%, transparent 14%),
      radial-gradient(circle at 90% 20%, var(--berry-blue) 0 3%, transparent 13%),
      radial-gradient(circle at 10% 80%, var(--berry-blue) 0 3%, transparent 14%),
      radial-gradient(circle at 88% 78%, var(--berry-blue) 0 3%, transparent 13%),
      linear-gradient(160deg, var(--leaf-green) 0%, #f2f6ee 45%, #f2f6ee 55%, var(--leaf-green) 100%);
    opacity: 0.85;
  }
  .disc {
    position: absolute;
    left: 22px;
    top: 53px;
    width: 536px;
    height: 566px;
    border-radius: 50%;
    background: var(--ring);
  }
  .disc-inner {
    position: absolute;
    inset: 7px;
    border-radius: 50%;
    background: linear-gradient(180deg, var(--disc-top) 0%, var(--disc-bottom) 60%, var(--disc-top) 100%);
  }
  .brand {
    position: absolute;
    left: 0;
    right: 0;
    top: 128px;
    text-align: center;
    font-family: "Barlow", sans-serif;
    font-weight: 600;
    font-size: 17px;
    letter-spacing: 3px;
    color: var(--brand);
    text-transform: uppercase;
  }
  .brand-dot {
    display: block;
    width: 22px;
    height: 22px;
    margin: 0 auto 10px;
    border-radius: 50%;
    background: var(--brand);
  }
  .product-name {
    position: absolute;
    left: 0;
    right: 0;
    top: 279px;
    margin: 0;
    text-align: center;
    font-family: "Questrial", sans-serif;
    font-weight: 400;
    font-size: 90px;
    line-height: 76px;
    color: var(--ink);
    letter-spacing: -1px;
  }
  .claims {
    position: absolute;
    left: 0;
    right: 0;
    text-align: center;
    font-family: "Barlow", sans-serif;
    font-weight: 600;
    color: var(--ink);
    margin: 0;
    letter-spacing: 1px;
  }
  .claims-primary { top: 450px; font-size: 27px; line-height: 35px; }
  .claims-secondary { top: 533px; font-size: 20px; line-height: 24px; }
  .size-chip {
    position: absolute;
    left: 176px;
    top: 639px;
    width: 222px;
    height: 37px;
    background: var(--size-chip);
    text-align: center;
    font-family: "Barlow", sans-serif;
    font-weight: 600;
    font-size: 25px;
    line-height: 37px;
    color: var(--ink);
    letter-spacing: 0.5px;
  }
</style>
</head>
<body>
  <main class="label">
    <div class="botanical-art" role="img" aria-label="Watercolour elderberry branches with dark berry clusters and green leaves"></div>
    <div class="disc"><div class="disc-inner"></div></div>
    <div class="brand"><span class="brand-dot"></span>Hollow Creek Tonics</div>
    <h1 class="product-name">Elderberry<br>Syrup</h1>
    <p class="claims claims-primary">ORGANIC INGREDIENTS<br>LOCAL HONEY</p>
    <p class="claims claims-secondary">COLD-FLU-ALLERGIES<br>NATURAL REMEDY</p>
    <div class="size-chip">8 fl oz/236 ml</div>
  </main>
</body>
</html>
```